Potential SF Gazette Best Seller Poetry Book Cover Contest

I’m penning my first poetry book. It’s entitled “Lanterns Under Rain”
I’m fairly open to creative freedom but I want the cover to without a doubt catch a persons' eye instantly because first impressions are VERY IMPORTANT in the literary world
I tend to lean towards a luxury look and colors like black, gold, rose gold, silver, glitter etc but again I’m open to interpretation
Looking forward to your submissions
Target Market(s)
those seeking relatable love advice and quotes
modern millenials
Colors
Look and feel

```html
<!DOCTYPE html>
<html lang="en">
<head>
<meta charset="utf-8">
<title>Lanterns Under Rain — Cover</title>
<link rel="stylesheet" href="https://fonts.googleapis.com/css2?family=Jost:wght@500&family=Sacramento&display=swap">
<style>
  :root {
    --page-bg: #ffffff;
    --paper: #e9e8e4;
    --paper-shade: #dedcd7;
    --ink: #0b0b0b;
    --rose: #c81a5c;
  }
  * { margin: 0; padding: 0; box-sizing: border-box; }
  html, body {
    width: 1018px;
    height: 1200px;
    overflow: hidden;
    background: var(--page-bg);
  }
  .canvas {
    position: relative;
    width: 1018px;
    height: 1200px;
    display: flex;
    align-items: center;
    justify-content: center;
  }
  .cover {
    position: relative;
    width: 760px;
    height: 1140px;
    background: radial-gradient(ellipse at 40% 40%, var(--paper) 0%, var(--paper-shade) 100%);
    overflow: hidden;
  }
  .ink-drip {
    position: absolute;
    top: 0;
    left: 0;
    width: 760px;
    height: 90px;
    display: block;
  }
  .title-script {
    position: absolute;
    left: 40px;
    top: 230px;
    font-family: "Sacramento", cursive;
    font-size: 118px;
    line-height: 100px;
    color: var(--rose);
  }
  .title-script span { display: block; }
  .title-script .line-2 { padding-left: 10px; }
  .title-main {
    position: absolute;
    left: 48px;
    top: 520px;
    font-family: "Jost", sans-serif;
    font-weight: 500;
    font-size: 268px;
    line-height: 1;
    letter-spacing: -4px;
    color: var(--ink);
  }
  .author {
    position: absolute;
    left: 40px;
    right: 40px;
    bottom: 70px;
    font-family: "Sacramento", cursive;
    font-size: 74px;
    line-height: 1;
    color: var(--ink);
    text-align: center;
  }
</style>
</head>
<body>
<main class="canvas">
  <section class="cover">
    <svg class="ink-drip" viewBox="0 0 760 90" role="img" aria-label="Black ink spilling and dripping down from the top edge of the cover">
      <defs>
        <linearGradient id="inkFade" x1="0" y1="0" x2="0" y2="1">
          <stop offset="0" stop-color="#0b0b0b"/>
          <stop offset="1" stop-color="#1e1e1e"/>
        </linearGradient>
      </defs>
      <rect x="0" y="0" width="760" height="90" fill="url(#inkFade)"/>
    </svg>

    <h1 class="title">
      <span class="title-script">
        <span class="line-1">Lanterns</span>
        <span class="line-2">under</span>
      </span>
      <span class="title-main">RAIN</span>
    </h1>

    <p class="author">Avery Quinn-Hollis</p>
  </section>
</main>
</body>
</html>
```